"Recently Leased" flyer for real estate agency

Looking to have a Recently Leased flyer designed. This will be delivered to apartments and houses closely situated to a property we have recently leased. The idea is to get the attention of owner/landlords in the area that may be considering leasing their property in the future and inform them of the great work we are doing locally. I would like the design to be a two sided flyer using the photoshop (PSD) template below (we would like to be able to edit this once complete should we need to update copy etc in the future). I would like the front page to look like our "for lease sign with the leased sticker on it and copy, I dont want it to look like a typical junk mail flyer.

Target Market(s)

Property owners and investors, male and female aged 28-70

Industry/Entity Type

Real Estate

Font styles to use
Sans Serif

Colors

Designer to choose colors to be used in the design.

Requirements
Must have
• Harbor Keystone Logo
• Contact information
• Copy supplied
Nice to have
• Slick, clean design,
Should not have
• too many colours or too busy a design.
• NO PROPERTY PHOTOS ON FRONT - I want this to be generic and not relate to a specific property image which might confuse people.

```html
<!DOCTYPE html>
<html lang="en">
<head>
<meta charset="utf-8">
<title>Harbor Keystone – Recently Leased Flyer</title>
<link rel="stylesheet" href="https://fonts.googleapis.com/css2?family=Roboto+Condensed:wght@300;400;700&display=swap">
<style>
:root{
  --stage:#c0c0c2;
  --teal:#137b8d;
  --teal-dark:#0f5f6e;
  --teal-light:#2a9fa8;
  --teal-name:#1a9aa6;
  --grey-tint:#e6e6e7;
  --ink:#111;
  --red:#c1272d;
  --white:#fff;
}
*{box-sizing:border-box;margin:0;padding:0}
html,body{width:1200px;height:1200px;overflow:hidden;background:var(--stage)}
body{position:relative;font-family:"Roboto Condensed",Arial,sans-serif}
.flyer{position:absolute;top:94px;width:462px;height:1004px;overflow:hidden;box-shadow:0 1px 3px rgba(0,0,0,.15)}
.flyer--front{left:86px;background:var(--white)}
.flyer--back{left:655px;background:var(--teal)}
.flyer__shapes{position:absolute;inset:0;width:100%;height:100%}
.abs{position:absolute}

/* front */
.leased-sticker{left:36px;top:32px;width:111px;height:26px;background:var(--red);border:2px solid var(--red);outline:1px solid var(--white);outline-offset:-4px;color:var(--white);font-size:22px;line-height:20px;text-align:center;letter-spacing:.5px}
.brand-name{left:0;width:462px;top:100px;text-align:center;font-size:38px;font-weight:700;color:var(--ink);letter-spacing:.3px}
.sign-icon{left:40px;top:224px;width:40px;height:42px}
.section-title{left:40px;top:270px;font-size:21px;font-weight:400;color:var(--teal)}
.intro{left:40px;top:305px;width:410px;font-size:12.4px;line-height:14.4px;color:var(--teal)}
.perks{left:40px;top:386px;width:400px;list-style:none}
.perk{position:absolute;left:0;display:flex;align-items:center;width:400px}
.perk svg{width:34px;height:34px;flex:none}
.perk span{margin-left:11px;font-size:15px;line-height:17.6px;color:var(--teal)}
.appraisal{right:30px;top:710px;width:290px;text-align:right;font-size:13.2px;line-height:15.3px;color:var(--teal)}

/* contact */
.contact{left:70px}
.contact__name{font-size:19px;font-weight:700;letter-spacing:.2px}
.contact__agency{font-size:14px;font-weight:700;margin-top:5px}
.contact__rows{list-style:none;margin-top:7px;position:relative}
.contact__rows::before{content:"";position:absolute;left:-9px;top:2px;bottom:2px;width:1px;background:currentColor;opacity:.7}
.contact__rows li{position:relative;font-size:15px;line-height:21.4px;height:21.4px;white-space:nowrap}
.contact__rows svg{position:absolute;left:-30px;top:5px;width:12px;height:12px}
.flyer--front .contact{top:826px;color:var(--white)}
.flyer--back .contact{left:61px;top:830px;color:var(--teal)}
.flyer--back .contact__name{color:var(--teal-name)}

/* back */
.headline{left:0;width:462px;top:48px;text-align:center;color:var(--white);font-size:29px;line-height:35px;font-weight:400}
.back-intro{left:31px;width:400px;top:184px;text-align:center;color:var(--white);font-size:12.8px;line-height:16px}
.benefits{list-style:none}
.benefit{position:absolute;left:28px;width:420px;display:flex;align-items:flex-start;color:var(--white)}
.benefit svg{width:34px;height:34px;flex:none}
.benefit span{margin-left:12px;font-size:13.8px;line-height:16px}
.closing{left:31px;width:400px;top:653px;text-align:center;color:var(--white);font-size:15.5px;line-height:16.4px}
.back-brand{right:42px;top:770px;color:var(--white);font-size:16px;font-weight:700}
</style>
</head>
<body>

<section class="flyer flyer--front">
  <svg class="flyer__shapes" viewBox="0 0 578 1255" preserveAspectRatio="none" aria-hidden="true">
    <polygon points="383,0 578,0 578,105" fill="var(--teal-light)"/>
    <polygon points="0,155 0,200 420,325" fill="var(--teal-light)"/>
    <polygon points="0,198 578,373 578,411" fill="var(--teal-dark)"/>
    <polygon points="578,790 578,1085 183,923" fill="var(--grey-tint)"/>
    <polygon points="0,868 578,1085 578,1255 0,1255" fill="var(--teal)"/>
    <polygon points="0,868 578,1085 0,913" fill="var(--teal-dark)"/>
    <polygon points="0,913 578,1085 0,943" fill="var(--teal-light)"/>
  </svg>

  <div class="abs leased-sticker">LEASED!</div>
  <div class="abs brand-name">HARBOR KEYSTONE</div>

  <svg class="abs sign-icon" viewBox="0 0 40 42" fill="none" stroke="var(--teal)" stroke-width="1.6">
    <path d="M3 2v38M3 5h36M1 40h8M13 40h4M21 40h4"/>
    <rect x="9" y="9" width="28" height="20" rx="2"/>
    <path d="M14 20l4-4 4 4v5h-8zM25 16h8M25 20h8M25 24h8"/>
  </svg>

  <h2 class="abs section-title">Recently Leased</h2>
  <p class="abs intro">We recently leased a property in your building or street.<br>Attracting a great reliable tenant and fantastic return for the owner.<br>We received a high number of enquiresand applications for this property and<br>have a database of screened and qualified tenants looking to lease in your area.</p>

  <ul class="abs perks">
    <li class="perk" style="top:5px"><svg viewBox="0 0 34 34"><path d="M2 6l10 11-10 11h7l10-11L9 6zM15 6l10 11-10 11h7l10-11L22 6z" fill="var(--teal)"/></svg><span>On average we lease properties 2 weeks<br>faster than the Northern Beaches average</span></li>
    <li class="perk" style="top:53px"><svg viewBox="0 0 34 34" fill="none" stroke="var(--teal)" stroke-width="3" stroke-linecap="round"><path d="M7 27L27 7M7 7l20 20"/><circle cx="25" cy="9" r="3"/></svg><span>Strong database of tenants actively<br>looking in the area</span></li>
    <li class="perk" style="top:100px"><svg viewBox="0 0 34 34"><path d="M18 4h12v12L14 32 2 20z" fill="var(--teal)"/><circle cx="25" cy="9" r="2" fill="var(--white)"/></svg><span>All we do is lease property, no sales – so tenanting<br>and managing your property is our priority</span></li>
    <li class="perk" style="top:149px"><svg viewBox="0 0 34 34" fill="var(--teal)"><circle cx="20" cy="5" r="3"/><path d="M17 9h6l3 9-4 1-2-5-3 6 4 5-2 8h-3l1-7-4-4-3 11H7l4-14z"/></svg><span>90 day money back guarantee on<br>our level of service</span></li>
    <li class="perk" style="top:197px"><svg viewBox="0 0 34 34" fill="none" stroke="var(--teal)" stroke-width="1.8"><circle cx="17" cy="7" r="4"/><path d="M17 11v10M13 21h8l2 11H11z"/></svg><span>Highly competitive, simple all-inclusive pricing.</span></li>
    <li class="perk" style="top:245px"><svg viewBox="0 0 34 34" fill="none" stroke="var(--teal)" stroke-width="2.2"><path d="M3 19L19 3l12 12-16 16z"/><path d="M10 19l9-9 5 5-9 9z"/></svg><span>Experience the difference of a property<br>management specialist</span></li>
  </ul>

  <p class="abs appraisal">Contact Sam to get your<br>free rental appraisal or transfer<br>your existing investment to an agency that<br>willgive it the attention it deserves<br>and maximise your return</p>

  <div class="abs contact">
    <div class="contact__name">SAM CARTER</div>
    <div class="contact__agency">Harbor Keystone Agency</div>
    <ul class="contact__rows">
      <li><svg viewBox="0 0 12 12"><path d="M6 0a4 4 0 0 0-4 4c0 3 4 8 4 8s4-5 4-8a4 4 0 0 0-4-4z" fill="currentColor"/><circle cx="6" cy="4" r="1.5" fill="var(--teal)"/></svg>Level 2, 18 Ferncliff Rd, Ashwood NSW 2099</li>
      <li><svg viewBox="0 0 12 12" fill="none" stroke="currentColor"><circle cx="6" cy="6" r="5.2"/><ellipse cx="6" cy="6" rx="2.3" ry="5.2"/><path d="M1 6h10M2 3h8M2 9h8"/></svg>www.harborkeystone.com.au</li>
      <li><svg viewBox="0 0 12 12"><path d="M2 0l2 3-1 2c1 2 2 3 4 4l2-1 3 2-1 2C5 12 0 7 0 1z" fill="currentColor"/></svg>0400 555 218</li>
      <li><svg viewBox="0 0 12 12"><path d="M0 2h12v1L6 7 0 3zM0 4.5l6 4 6-4V11H0z" fill="currentColor"/></svg>sam@harborkeystone.com.au</li>
    </ul>
  </div>
</section>

<section class="flyer flyer--back">
  <svg class="flyer__shapes" viewBox="0 0 578 1255" preserveAspectRatio="none" aria-hidden="true">
    <polygon points="381,0 578,0 578,105" fill="var(--teal-dark)"/>
    <polygon points="578,803 578,1098 181,943" fill="var(--teal-dark)"/>
    <polygon points="0,883 0,930 578,1098" fill="var(--teal-light)"/>
    <polygon points="0,953 578,1098 578,1255 0,1255" fill="var(--white)"/>
  </svg>

  <h1 class="abs headline">PROPERTY<br>MANAGEMENT<br>DONE RIGHT!</h1>
  <p class="abs back-intro">The fundamental idea behind Harbor Keystone Agency was to give landlords a simple and confidence inspiring experience. We achieve this through:</p>

  <ul class="benefits">
    <li class="benefit" style="top:268px"><svg viewBox="0 0 34 34" fill="none" stroke="var(--white)" stroke-width="1.3"><circle cx="17" cy="7" r="4"/><path d="M10 18c1-4 13-4 14 0zM4 24l2 3 3 0-2 2 1 3-3-2-3 2 1-3-2-2h3zM14 24l2 3h3l-2 2 1 3-3-2-3 2 1-3-2-2h3zM26 24l2 3h3l-2 2 1 3-3-2-3 2 1-3-2-2h3z"/></svg><span>Unique marketing that goes beyond the standard<br>listing sites and has seen our average days-on-market<br>at 5.9 days for 2018.</span></li>
    <li class="benefit" style="top:334px"><svg viewBox="0 0 34 34"><circle cx="17" cy="17" r="15" fill="var(--white)"/><path d="M22 9c-6-2-11 2-6 7s1 10-6 8" stroke="var(--teal)" stroke-width="3" fill="none"/></svg><span style="margin-top:9px">A simple, yet competitive fee structure.</span></li>
    <li class="benefit" style="top:381px"><svg viewBox="0 0 34 34" fill="var(--white)"><circle cx="12" cy="12" r="8"/><circle cx="25" cy="24" r="6"/><circle cx="12" cy="12" r="3" fill="var(--teal)"/><circle cx="25" cy="24" r="2" fill="var(--teal)"/></svg><span>Excellent customer service through an experienced<br>professional property manager.</span></li>
    <li class="benefit" style="top:437px"><svg viewBox="0 0 34 34" fill="var(--white)"><path d="M2 6l10 2v6L2 12z"/><circle cx="24" cy="6" r="3"/><rect x="20" y="11" width="8" height="20" rx="2"/></svg><span>Sound advice and communication through out the<br>leasing and management process.</span></li>
    <li class="benefit" style="top:488px"><svg viewBox="0 0 34 34" fill="none" stroke="var(--white)" stroke-width="3" stroke-linecap="round"><path d="M17 3v13M10 8a12 12 0 1 0 14 0"/></svg><span>A simple yet powerful landlord portal which enables<br>owners to view media rich inspection reports,<br>financial reports and maintenance progress at anytime.</span></li>
    <li class="benefit" style="top:556px"><svg viewBox="0 0 34 34" fill="none" stroke="var(--white)" stroke-width="1.3"><circle cx="19" cy="11" r="7"/><path d="M19 7v8M2 24l6-3 8 2h6l7-4c2 0 2 2 0 3l-8 6H9l-7 1"/></svg><span>We then back our service promise with a 90day<br>money back guarantee.</span></li>
  </ul>

  <p class="abs closing">If you have been considering leasing your property, purchasing alocal investment or aren’t happy with your current managing agency, please don’t hesitate to contact your local rental specialist for more information:</p>

  <div class="abs back-brand">HARBOR KEYSTONE</div>

  <div class="abs contact">
    <div class="contact__name">SAM CARTER</div>
    <div class="contact__agency">Harbor Keystone Agency</div>
    <ul class="contact__rows">
      <li><svg viewBox="0 0 12 12"><path d="M6 0a4 4 0 0 0-4 4c0 3 4 8 4 8s4-5 4-8a4 4 0 0 0-4-4z" fill="currentColor"/><circle cx="6" cy="4" r="1.5" fill="var(--white)"/></svg>Level 2, 18 Ferncliff Rd, Ashwood NSW 2099</li>
      <li><svg viewBox="0 0 12 12" fill="none" stroke="currentColor"><circle cx="6" cy="6" r="5.2"/><ellipse cx="6" cy="6" rx="2.3" ry="5.2"/><path d="M1 6h10M2 3h8M2 9h8"/></svg>www.harborkeystone.com.au</li>
      <li><svg viewBox="0 0 12 12"><path d="M2 0l2 3-1 2c1 2 2 3 4 4l2-1 3 2-1 2C5 12 0 7 0 1z" fill="currentColor"/></svg>0400 555 218</li>
      <li><svg viewBox="0 0 12 12"><path d="M0 2h12v1L6 7 0 3zM0 4.5l6 4 6-4V11H0z" fill="currentColor"/></svg>sam@harborkeystone.com.au</li>
    </ul>
  </div>
</section>

</body>
</html>
```